FSA Expiring Soon 2023

Hi,
Looking to upgrade the design of current flyer to be used as an e-blast.
-8.5"x11"
-Under 5MB
-Several formats, PDF, .ai, jpeg, png

This flyer should be simple, yet eye catching. The goal is to remind patients that their Flexible Spending Account (FSA) will be expiring soon and that they can use their FSA or HSA to purchase most of our over the counter items, including inserts and shoes.

-must include: Some insurance plans require a letter of medical necessity
-must include: Each flexible spending account varies on their expiration date
- stock images must be free

I'll attach our logo and old flyer as well for reference.

Thank you,
Oscar

```html
<!DOCTYPE html>
<html lang="en">
<head>
<meta charset="utf-8">
<title>FSA Expiring Soon – Ridgeview Foot &amp; Ankle</title>
<link href="https://fonts.googleapis.com/css2?family=Montserrat:ital,wght@0,500;0,600;0,700;0,800;0,900;1,600&family=Red+Hat+Display:wght@400;500;700&display=swap" rel="stylesheet">
<style>
  :root{
    --stage:#e9e6e1;
    --white:#ffffff;
    --orange:#f47a3c;
    --orange-dark:#d95f28;
    --teal:#52c3a3;
    --blue:#4fb3d2;
    --rule:#dcdcdc;
    --black:#050505;
    --photo-wood:#a9764a;
    --photo-block:#d9b17e;
    --photo-wall:#eeeae6;
  }
  *{margin:0;padding:0;box-sizing:border-box}
  html,body{width:1200px;height:1117px;overflow:hidden;background:var(--stage)}
  body{font-family:"Red Hat Display",sans-serif;position:relative}
  .flyer{position:absolute;left:178px;top:20px;width:845px;height:1077px;background:var(--white);overflow:hidden}
  .abs{position:absolute}

  .brand{position:absolute;left:80px;right:100px;top:36px;display:flex;align-items:center;justify-content:flex-end;gap:26px}
  .brand-mark{width:26px;height:26px;border-radius:50%;background:var(--teal);flex:none}
  .brand-name{font-family:"Montserrat",sans-serif;font-weight:800;color:var(--orange);text-align:right;line-height:1.02;font-size:46px;letter-spacing:-0.5px}
  .brand-name small{display:block;font-size:24px;margin-top:8px;letter-spacing:0}

  .rule{left:88px;top:225px;width:668px;height:2px;background:var(--rule)}

  .photo{left:0;top:258px;width:845px;height:316px;
    background:linear-gradient(180deg,var(--photo-wall) 0%,var(--photo-wall) 22%,var(--photo-block) 40%,var(--photo-block) 72%,var(--photo-wood) 100%)}
  .photo-mask{left:0;top:240px;width:845px;height:100px}

  .headline-soon{left:0;width:845px;top:240px;padding-left:364px;font-family:"Montserrat",sans-serif;font-weight:800;font-size:38px;letter-spacing:-0.5px}
  .headline-soon .t{color:var(--teal)} .headline-soon .b{color:var(--blue)}

  .band{left:0;top:574px;width:845px;height:300px;background:linear-gradient(200deg,var(--teal) 35%,var(--blue) 100%)}
  .band-title{left:0;top:597px;width:845px;text-align:center;color:var(--white);font-family:"Montserrat",sans-serif;font-weight:900;font-size:23.5px;line-height:28px;letter-spacing:-0.2px}
  .band-copy{left:0;top:656px;width:845px;text-align:center;color:var(--white);font-size:18.5px;line-height:20px}
  .reminder{left:108px;top:709px;width:628px;height:44px;border-radius:22px;background:var(--white);
    box-shadow:0 10px 14px -8px rgba(0,0,0,.25);display:flex;align-items:center;justify-content:center;
    color:var(--orange);font-weight:700;font-size:18.5px}

  .base{left:0;top:760px;width:845px;height:230px}
  .notice{left:420px;top:808px;width:270px;text-align:center;color:var(--white);font-family:"Montserrat",sans-serif;font-style:italic;font-weight:600;font-size:14px;line-height:18px}

  .offices{left:78px;top:864px;width:688px;display:flex;justify-content:space-between}
  .office{width:203px;text-align:center;color:var(--white)}
  .office-name{height:35px;border-radius:18px;background:var(--orange-dark);display:flex;align-items:center;justify-content:center;font-family:"Montserrat",sans-serif;font-weight:600;font-size:15.5px}
  .office-address{margin-top:12px;font-family:"Montserrat",sans-serif;font-weight:600;font-size:15.5px;line-height:20px}
  .divider{top:863px;width:2px;height:101px;background:var(--orange-dark);opacity:.7}

  .footer{left:0;top:990px;width:845px;height:87px;background:var(--black);display:flex;align-items:center;justify-content:center;gap:20px;color:var(--white);font-family:"Montserrat",sans-serif;font-weight:600;font-size:27px}
  .contact{display:flex;align-items:center;gap:14px}
  .icon{width:32px;height:32px;border-radius:50%;background:linear-gradient(135deg,var(--teal),var(--blue));display:flex;align-items:center;justify-content:center}
  .footer-sep{width:2px;height:44px;background:var(--orange)}
</style>
</head>
<body>
<main class="flyer">
  <header class="brand">
    <span class="brand-mark"></span>
    <div class="brand-name">RIDGEVIEW<br>FOOT &amp; ANKLE<small>STRIDEWELLFEET.COM</small></div>
  </header>
  <div class="abs rule"></div>

  <div class="abs photo" role="img" aria-label="Photo of wooden letter cubes spelling FSA and HSA on a wooden table"></div>
  <svg class="abs photo-mask" viewBox="0 0 845 100" preserveAspectRatio="none" aria-hidden="true">
    <path d="M0 0 H845 V18 C760 50 690 92 590 92 C420 92 200 40 0 18 Z" fill="var(--white)"/>
  </svg>
  <h1 class="abs headline-soon"><span class="t">EXPIRING</span> <span class="b">SOON!</span></h1>

  <section class="abs band"></section>
  <h2 class="abs band-title">USE YOUR FLEXIBLE SPENDING ACCOUNT FUNDS<br>BEFORE THEY EXPIRE AT THE END OF THE YEAR!</h2>
  <p class="abs band-copy">most of our over the counter products are FSA/HSA eligible,<br>including inserts and shoes.</p>
  <p class="abs reminder">Each flexible spending account varies on their expiration date</p>

  <svg class="abs base" viewBox="0 0 845 230" preserveAspectRatio="none" aria-hidden="true">
    <path d="M0 30 L213 54 L540 12 C585 4 610 4 650 14 L845 72 V230 H0 Z" fill="var(--white)"/>
    <path d="M0 96 L540 28 C585 20 610 18 650 30 L845 86 V230 H0 Z" fill="var(--orange)"/>
  </svg>
  <p class="abs notice">Some insurance<br>plans require a letter of medical necessity</p>

  <section class="abs offices">
    <div class="office">
      <div class="office-name">Ridgeview Office</div>
      <p class="office-address">215 Aldergate<br>Dr. Ste. 140<br>Ridgeview, MD 21790</p>
    </div>
    <div class="office">
      <div class="office-name">Maple Hill Office</div>
      <p class="office-address">4810 Larkspur<br>Blvd. Ste. 305<br>Maple Hill, MD 21795</p>
    </div>
    <div class="office">
      <div class="office-name">Cedar Falls Office</div>
      <p class="office-address">86 Wellness Way<br>Cedar Falls,<br>WV 25498</p>
    </div>
  </section>
  <div class="abs divider" style="left:301px"></div>
  <div class="abs divider" style="left:543px"></div>

  <footer class="abs footer">
    <div class="contact">
      <span class="icon">
        <svg width="20" height="20" viewBox="0 0 20 20" fill="none" stroke="#0c2a33" stroke-width="1.6" aria-hidden="true">
          <circle cx="10" cy="10" r="8"/><ellipse cx="10" cy="10" rx="3.5" ry="8"/><path d="M2 10h16M3.5 5.5h13M3.5 14.5h13"/>
        </svg>
      </span>
      StrideWellFeet.com
    </div>
    <span class="footer-sep"></span>
    <div class="contact">
      <span class="icon">
        <svg width="18" height="18" viewBox="0 0 24 24" aria-hidden="true">
          <path fill="#0c2a33" d="M6.6 10.8a15.2 15.2 0 0 0 6.6 6.6l2.2-2.2a1 1 0 0 1 1-.25 11.4 11.4 0 0 0 3.6.57 1 1 0 0 1 1 1V20a1 1 0 0 1-1 1A17 17 0 0 1 3 4a1 1 0 0 1 1-1h3.5a1 1 0 0 1 1 1c0 1.25.2 2.45.57 3.57a1 1 0 0 1-.25 1z"/>
        </svg>
      </span>
      (877)555-0142
    </div>
  </footer>
</main>
</body>
</html>
```